Web Header needed for an inspirational coaching company's website - ongoing work

We need a beautifully designed web header to replace my current one at my homepage on my website www.kelvoria.com
There will be continuous work required for various creative work in the future if your work is selected.
I work with corporate professionals and executives to bring clarity and joy back to their career. It needs to be elegant, sophisticated, intelligent, but friendly and inspiring at the same time.
Thank you!
Target Market(s)
Corporate profesionals and executives
Industry/Entity Type
It Company
Colors
Designer to choose colors to be used in the design.
Look and feel

```html
<!DOCTYPE html>
<html lang="en">
<head>
<meta charset="utf-8">
<title>Bring Clarity to Your Career</title>
<link rel="stylesheet" href="https://fonts.googleapis.com/css2?family=Open+Sans:wght@300;400;700&display=swap">
<style>
  :root {
    --teal-mid: #3a6a70;
    --teal-deep: #1f4047;
    --teal-darkest: #142e33;
    --glow: rgba(220, 240, 240, 0.5);
    --portrait-dark: #2b2527;
    --portrait-warm: #8c5a47;
    --portrait-accent: #d9531f;
    --headline: #ffffff;
  }
  * { margin: 0; padding: 0; box-sizing: border-box; }
  html, body { width: 1200px; height: 539px; overflow: hidden; }
  body { font-family: "Open Sans", Arial, sans-serif; }

  .hero-header {
    position: relative;
    width: 1200px;
    height: 539px;
    overflow: hidden;
    background:
      radial-gradient(ellipse 360px 230px at 560px 0px, rgba(110, 170, 178, 0.75), transparent 70%),
      radial-gradient(ellipse 230px 200px at 210px 200px, rgba(110, 150, 150, 0.35), transparent 75%),
      linear-gradient(180deg, var(--teal-mid) 0%, var(--teal-deep) 60%, var(--teal-darkest) 100%);
  }

  .coach-portrait {
    position: absolute;
    left: 140px;
    top: 152px;
    width: 292px;
    height: 410px;
    border-radius: 24px 24px 0 0;
    background: linear-gradient(170deg,
      var(--portrait-dark) 0%,
      var(--portrait-warm) 55%,
      var(--portrait-accent) 100%);
    box-shadow: 0 0 14px 4px var(--glow);
  }

  .headline {
    position: absolute;
    right: 226px;
    top: 227px;
    color: var(--headline);
    text-align: right;
    font-size: 62px;
    line-height: 62px;
    letter-spacing: -2.5px;
    font-weight: 300;
  }
  .headline strong { font-weight: 700; }
  .headline .line { display: block; white-space: nowrap; }
  .headline .connector {
    font-size: 44px;
    letter-spacing: -1.5px;
    vertical-align: 16px;
    margin-right: 1px;
  }
</style>
</head>
<body>
  <header class="hero-header">
    <div class="coach-portrait" role="img" aria-label="Portrait photo of a smiling career coach in an orange top"></div>
    <h1 class="headline">
      <span class="line">Bring <strong>Clarity</strong></span>
      <span class="line"><span class="connector">to</span>Your <strong>Career</strong></span>
    </h1>
  </header>
</body>
</html>
```